Home Care company needs letter head branding

Home care company needs a letter head which can be used for all documents the company's clients view. We provided in home care for the elderly. We would like to use our company colors (2785A7, 0A4057 and 34A74D) and should not be too large as we will be using it on more than just a letter head but all documents our clients sign / receive.
Target Market(s)
Professional business
Industry/Entity Type
Health Care
Requirements
Must have
- corporate brand colors

```html
<!DOCTYPE html>
<html lang="en">
<head>
<meta charset="utf-8">
<title>Elmbrook Care Letterhead</title>
<link href="https://fonts.googleapis.com/css2?family=Montserrat:wght@600;700&display=swap" rel="stylesheet">
<style>
  :root {
    --brand-teal: #2785A7;
    --brand-navy: #0A4057;
    --brand-lime: #b5d334;
    --paper: #ffffff;
    --footer-text: #ffffff;
  }
  html, body {
    margin: 0;
    padding: 0;
    overflow: hidden;
    background: var(--paper);
  }
  .letterhead {
    position: relative;
    width: 954px;
    height: 1200px;
    overflow: hidden;
    background: linear-gradient(180deg, #ffffff 0%, #ffffff 60%, #fcfcfc 100%);
    font-family: "Montserrat", Arial, sans-serif;
  }
  .brand {
    position: absolute;
    top: 2px;
    left: 466px;
    display: flex;
    align-items: center;
    gap: 14px;
  }
  .brand-mark {
    width: 96px;
    height: 96px;
    border-radius: 50%;
    border: 5px solid var(--brand-teal);
    box-sizing: border-box;
  }
  .brand-name {
    font-size: 40px;
    font-weight: 700;
    color: var(--brand-teal);
    letter-spacing: -0.5px;
    white-space: nowrap;
  }
  .accent-line {
    position: absolute;
    left: 0;
    top: 1108px;
    width: 954px;
    height: 16px;
    background: linear-gradient(90deg, rgba(181,211,52,0) 10%, rgba(181,211,52,0.35) 45%, var(--brand-lime) 100%);
  }
  .footer {
    position: absolute;
    left: 0;
    top: 1124px;
    width: 954px;
    height: 76px;
    background: linear-gradient(90deg, var(--brand-teal) 0%, #1e6f8e 50%, var(--brand-navy) 100%);
    color: var(--footer-text);
    overflow: hidden;
  }
  .footer-ring {
    position: absolute;
    left: 26px;
    top: 6px;
    width: 92px;
    height: 92px;
    border-radius: 50%;
    border: 4px solid rgba(255,255,255,0.3);
    box-sizing: border-box;
  }
  .footer-address {
    position: absolute;
    left: 140px;
    width: 300px;
    top: 15px;
    text-align: center;
    font-size: 17px;
    font-weight: 700;
    line-height: 22px;
  }
  .footer-divider {
    position: absolute;
    top: 18px;
    width: 3px;
    height: 38px;
    background: var(--footer-text);
  }
  .footer-divider.first { left: 451px; }
  .footer-divider.second { left: 623px; }
  .footer-phone {
    position: absolute;
    left: 460px;
    width: 160px;
    top: 26px;
    text-align: center;
    font-size: 17px;
    font-weight: 700;
  }
  .footer-web {
    position: absolute;
    left: 648px;
    top: 27px;
    font-size: 16px;
    font-weight: 700;
    letter-spacing: 2.6px;
    white-space: nowrap;
  }
</style>
</head>
<body>
  <div class="letterhead">
    <header class="brand">
      <div class="brand-mark" aria-hidden="true"></div>
      <div class="brand-name">Elmbrook Care</div>
    </header>

    <div class="accent-line" aria-hidden="true"></div>

    <footer class="footer">
      <div class="footer-ring" aria-hidden="true"></div>
      <div class="footer-address">2290 Larkfield Ave, Suite B140<br>Rockmont MD 20734</div>
      <div class="footer-divider first" aria-hidden="true"></div>
      <div class="footer-phone">(301) 555-0142</div>
      <div class="footer-divider second" aria-hidden="true"></div>
      <div class="footer-web">www.elmbrookcare.com</div>
    </footer>
  </div>
</body>
</html>
```